Plakat-Design für Blasmusik Konzert
Zielgruppe
Wir - die Tordinger Blasmusik e.V. - sind auf der Suche nach:
einem Plakatdesign in A1 & A2 und passendem
Ticket-Design DIN lang quer inkl. Perforierung und 2x Nummerierung
für unser Konzert 2019 mit dem Motto:
'NIGHTS OF WONDER'.
Das Konzert wird einen weiten Rahmen von Henrik Dallmann und Brisko hin zu Bernd Falkenrath und Tom Kellin. Auch Titel aus dem Bereich Filmmusik wird es geben. Also ein bunter Abend mit Gesang und Showlicht.
Wir freuen uns auf eure Ideen!!!
Impressionen: www.tordinger-blasmusik.de
Aufgabenstellung
Stichworte: Bunt, Modern, Edel
Facts:
Samstag 05.10.2019 Beginn 19:00
Aula im Lernzentrum, Tordingen am See
Eintritt 15€, Kinder bis einschließlich 8 Jahre Eintritt frei.
'Mehr Informationen unter www.tordinger-blasmusik.de und auf Plaudernet'
Für Ticket: Einlass ab 18:30 Uhr. Freie Platzwahl.
Irgendwo auf dem Plakat muss Platz für die dezente Nennung von 2-3 Sponsoren vorgesehen werden. Diese würden wir nachträglich einfügen. Auch ein 'Find us on Plaudernet'-Icon wäre cool.
Die Druckdateien (CMYK) sind mit entsprechendem Beschnitt gemäß Vorgabe von 'flott-gedruckt-jetzt' anzulegen und als Vector-Datei sowie PDF zu übergeben.

```html
<!DOCTYPE html>
<html lang="de">
<head>
<meta charset="utf-8">
<title>Nights of Wonder – Plakat</title>
<link href="https://fonts.googleapis.com/css2?family=Inter:wght@500;600;700;800&display=swap" rel="stylesheet">
<style>
  :root {
    --backdrop: #3b3b3d;
    --wine: #8b1c24;
    --ink: #1a1a1a;
    --paper: #ffffff;
    --royal: #0d4a9a;
    --text-dark: #1d1d1d;
    --photo-hot: #e2604f;
    --photo-warm: #c23a4a;
    --photo-deep: #5a1a3a;
    --photo-gold: #d9a24a;
  }
  * { margin: 0; padding: 0; box-sizing: border-box; }
  html, body {
    width: 1200px; height: 1114px; overflow: hidden;
    background: var(--backdrop);
    font-family: "Inter", Arial, sans-serif;
  }
  .poster {
    position: absolute; left: 231px; top: 37px;
    width: 738px; height: 1040px;
    background: var(--paper);
    overflow: hidden;
  }
  .hero {
    position: absolute; left: 0; top: 0;
    width: 738px; height: 752px;
    background: var(--wine);
  }
  .hero-photo { position: absolute; left: 0; top: 0; }
  .title {
    position: absolute; left: 50px; bottom: 24px;
    writing-mode: vertical-rl;
    transform: rotate(180deg);
    color: var(--paper);
    font-weight: 700;
    font-size: 112px;
    line-height: 118px;
    letter-spacing: -1px;
    text-transform: uppercase;
  }
  .facts {
    position: absolute; left: 0; top: 752px;
    width: 738px; height: 181px;
    background: var(--ink);
    padding: 28px 0 0 50px;
  }
  .facts-date {
    color: var(--paper);
    font-weight: 600; font-size: 36px; line-height: 44px;
    letter-spacing: 0.2px;
  }
  .facts-venue {
    color: var(--royal);
    font-weight: 600; font-size: 35px; line-height: 45px;
  }
  .footer {
    position: absolute; left: 0; top: 933px;
    width: 738px; height: 107px;
    background: var(--paper);
    display: flex; align-items: center;
  }
  .club-name {
    width: 291px; padding-left: 54px;
    color: var(--wine);
    font-weight: 800; font-size: 22px; line-height: 25px;
  }
  .info {
    color: var(--text-dark);
    font-weight: 600; font-size: 15.5px; line-height: 19px;
  }
  .info a { color: var(--wine); text-decoration: underline; }
</style>
</head>
<body>
  <main class="poster">
    <section class="hero">
      <svg class="hero-photo" width="738" height="752" viewBox="0 0 738 752" role="img" aria-label="Konzertfoto: Saxophon in warmem Bühnenlicht, Nahaufnahme">
        <defs>
          <linearGradient id="stageLight" x1="0" y1="0" x2="1" y2="1">
            <stop offset="0" stop-color="var(--photo-deep)"/>
            <stop offset="0.35" stop-color="var(--photo-warm)"/>
            <stop offset="0.7" stop-color="var(--photo-hot)"/>
            <stop offset="1" stop-color="var(--photo-gold)"/>
          </linearGradient>
        </defs>
        <path d="M230 0 L738 0 L738 718 C640 722 560 712 480 690 C400 662 330 640 268 580 C262 470 250 360 246 260 C240 160 236 80 230 0 Z" fill="url(#stageLight)"/>
      </svg>
      <h1 class="title">Nights of<br>Wonder</h1>
    </section>
    <section class="facts">
      <p class="facts-date">SAMSTAG 05.10.2019 | BEGINN 19:00</p>
      <p class="facts-venue">AULA IM LERNZENTRUM,<br>TORDINGEN AM SEE</p>
    </section>
    <footer class="footer">
      <div class="club-name">Tordinger<br>Blasmusik e.V.</div>
      <p class="info">
        Eintritt 15€, Kinder bis einschließlich 8 Jahre Eintritt frei.<br>
        Mehr Informationen unter <a href="#">www.tordinger-blasmusik.de</a><br>
        und auf Plaudernet
      </p>
    </footer>
  </main>
</body>
</html>
```